Brave Otter Pet Sitting Postcard

I will be sending these postcards to homes in the neighborhood introducing my pet sitting business.

Include the following on the postcard:
Rosalind Hume
555-318-7294
www.braveotterpetsitting.example
help@braveotterpetsitting.example

```html
<!DOCTYPE html>
<html lang="en">
<head>
<meta charset="utf-8">
<title>Brave Otter Pet Sitting Postcard</title>
<link rel="stylesheet" href="https://fonts.googleapis.com/css2?family=Didact+Gothic&display=swap">
<style>
  :root {
    --page-bg: #eef1f1;
    --card-bg: #ffffff;
    --band-orange: #f5a537;
    --heading-orange: #f5a537;
    --ink: #1e1e1e;
    --teal: #1fa89a;
    --red: #e0192f;
    --blue: #1d6fb8;
    --brand-circle: #f5a537;
  }
  * { box-sizing: border-box; margin: 0; padding: 0; }
  html, body {
    width: 1200px; height: 1200px; overflow: hidden;
    background: var(--page-bg);
    font-family: "Didact Gothic", "Helvetica Neue", Arial, sans-serif;
    color: var(--ink);
  }
  .postcard {
    position: absolute; left: 0; top: 220px;
    width: 1200px; height: 760px;
    background: var(--card-bg);
  }
  .tagline-band {
    height: 123px; background: var(--band-orange);
    display: flex; align-items: center; justify-content: center;
  }
  .tagline {
    color: #fff; font-size: 60px; letter-spacing: 0.28em; font-weight: 400;
    padding-left: 0.28em;
  }
  .brand {
    position: absolute; left: 40px; top: 160px; width: 390px;
    display: flex; flex-direction: column; align-items: center;
  }
  .brand-mark {
    width: 230px; height: 230px; border-radius: 50%;
    background: var(--brand-circle);
  }
  .brand-name {
    margin-top: 26px; font-size: 34px; color: var(--ink); text-align: center;
  }
  .contact-person {
    position: absolute; left: 40px; top: 588px; width: 390px; text-align: center;
  }
  .contact-cta { color: var(--teal); font-size: 28px; letter-spacing: 0.02em; }
  .contact-name { color: var(--red); font-size: 40px; margin-top: 12px; letter-spacing: 0.03em; }
  .contact-phone { color: var(--red); font-size: 38px; margin-top: 2px; letter-spacing: 0.04em; }
  .responsibilities {
    position: absolute; left: 478px; top: 172px; width: 640px;
  }
  .section-title {
    display: flex; align-items: center; gap: 10px;
    color: var(--heading-orange); font-size: 38px; letter-spacing: 0.04em;
  }
  .section-title svg { width: 24px; height: 22px; }
  .intro {
    margin: 26px 0 0 32px; font-size: 22px; line-height: 27px; letter-spacing: 0.04em;
  }
  .task-group {
    display: flex; gap: 20px; margin: 18px 0 0 28px;
    font-size: 22px; line-height: 27px; letter-spacing: 0.04em;
  }
  .task-bullet {
    flex: 0 0 36px; width: 36px; height: 36px; border-radius: 50%;
    background: var(--band-orange); margin-top: -4px;
  }
  .task-list { list-style: none; }
  .web-contact {
    position: absolute; left: 600px; top: 600px; width: 540px; text-align: center;
    color: var(--blue);
  }
  .web-contact .link { font-size: 32px; line-height: 44px; letter-spacing: 0.03em; }
  .web-contact .credentials { font-size: 25px; margin-top: 4px; letter-spacing: 0.04em; }
</style>
</head>
<body>
  <article class="postcard">
    <header class="tagline-band">
      <h1 class="tagline">We care about your pet!</h1>
    </header>

    <div class="brand">
      <div class="brand-mark"></div>
      <div class="brand-name">Brave Otter Pet Sitting</div>
    </div>

    <section class="responsibilities">
      <h2 class="section-title">
        <svg viewBox="0 0 24 22" aria-hidden="true"><path d="M12 21 L2.5 11.5 A5.5 5.5 0 0 1 12 3.5 A5.5 5.5 0 0 1 21.5 11.5 Z" fill="var(--red)"/></svg>
        Responsibilities
      </h2>
      <p class="intro">We are responsible for all basic animal care while their clients are on vacation or traveling for business. They must be able to perform the following tasks:</p>
      <div class="task-group">
        <span class="task-bullet"></span>
        <ul class="task-list">
          <li>Provide food and water.</li>
          <li>Brush fur and teeth.</li>
          <li>Walk dogs.</li>
          <li>Clean litter boxes.</li>
          <li>Give medications, if applicable.</li>
        </ul>
      </div>
      <div class="task-group">
        <span class="task-bullet"></span>
        <p>Pet sitters provide daily care for pets while their owners are on vacation.</p>
      </div>
    </section>

    <div class="contact-person">
      <div class="contact-cta">CONTACT US NOW</div>
      <div class="contact-name">ROSALIND HUME</div>
      <div class="contact-phone">555•318•7294</div>
    </div>

    <div class="web-contact">
      <div class="link">help@braveotterpetsitting.example</div>
      <div class="link">www.braveotterpetsitting.example</div>
      <div class="credentials">Certified, Insured &amp; Bonded</div>
    </div>
  </article>
</body>
</html>
```